IT Services company

we want a modern card design that combines business and technology whilst not being too loud

the Company Name is Corvane Hub and i have attached the logo

can you also put the words Business Enabled Technology under the logo

thanks

Hi can you please show the card with a web url and contact name and email and phone number please

Business

```html
<!DOCTYPE html>
<html lang="en">
<head>
<meta charset="utf-8">
<title>Corvane Hub — Business Card</title>
<link rel="stylesheet" href="https://fonts.googleapis.com/css2?family=Source+Sans+3:wght@400&display=swap">
<style>
  :root {
    --card-bg: #2b2b2b;
    --accent-red: #9b0000;
    --mark-red: #c4100f;
    --text-light: #f2f2f2;
    --divider: #050505;
  }
  html, body {
    margin: 0;
    padding: 0;
    width: 1200px;
    height: 686px;
    overflow: hidden;
    background: var(--card-bg);
  }
  .card {
    position: relative;
    width: 1200px;
    height: 686px;
    background: var(--card-bg);
    font-family: "Source Sans 3", "Myriad Pro", Arial, sans-serif;
    color: var(--text-light);
    overflow: hidden;
  }
  .edge-band {
    position: absolute;
    left: 0;
    top: 0;
    width: 18px;
    height: 100%;
    background: var(--accent-red);
  }
  .brand-mark {
    position: absolute;
    left: 69px;
    top: 221px;
    width: 114px;
    height: 114px;
  }
  .brand-name {
    position: absolute;
    left: 217px;
    top: 248px;
    margin: 0;
    font-size: 50px;
    font-weight: 400;
    line-height: 1;
    letter-spacing: 0.5px;
    color: var(--text-light);
    white-space: nowrap;
  }
  .tagline {
    position: absolute;
    left: 216px;
    top: 318px;
    margin: 0;
    font-size: 51px;
    font-weight: 400;
    line-height: 48px;
    white-space: nowrap;
  }
  .divider {
    position: absolute;
    left: 616px;
    top: 215px;
    width: 4px;
    height: 125px;
    background: var(--divider);
  }
  .contact {
    position: absolute;
    left: 663px;
    top: 198px;
    margin: 0;
    font-style: normal;
    white-space: nowrap;
  }
  .contact-name {
    display: block;
    font-size: 60px;
    line-height: 64px;
  }
  .contact-line {
    display: block;
    font-size: 44px;
    line-height: 56.5px;
  }
</style>
</head>
<body>
  <div class="card">
    <div class="edge-band"></div>

    <svg class="brand-mark" viewBox="0 0 114 114" aria-hidden="true">
      <circle cx="57" cy="57" r="57" fill="var(--mark-red)"/>
    </svg>
    <h1 class="brand-name">Corvane Hub</h1>

    <p class="tagline">business<br>enabled<br>technology</p>

    <div class="divider"></div>

    <address class="contact">
      <span class="contact-name">john doe</span>
      <span class="contact-line">corvane hub</span>
      <span class="contact-line">p-555.555.555</span>
      <span class="contact-line">e-jdoe@corvanehub.com</span>
      <span class="contact-line">f-555.555.555</span>
    </address>
  </div>
</body>
</html>
```